Poster Design Project

Poster with modern feeling to be displayed in office. The text that needs to be included in this poster is below:

Rules
1. If it’s not in writing it doesn’t exist.
2. No such thing as 'off the record.'
3. Do not hold a private conversation in a public place.
4. Don’t believe any number that ends in zero.
5. Never turn down an opportunity to eat or go to the bathroom.
6. Don’t spend any of your own money. Don’t even admit you own a credit card. Don’t spend money that is not yours.
7. Not always a 'right' or 'wrong' answer - 'It depends.'
8. In a campaign, someone has to be in charge – campaigns are a place to foster democracy, not practice it.
9. Assume nothing.
10. If you make a mistake, fix it before analyzing. Bad news doesn’t age well.

Industry/Entity Type

Credit Card

Requirements
Must have
• Rules
7. Not always a “right” or “wrong” answer - 'It depends.' 
9. Assume nothing.

```html
<!DOCTYPE html>
<html lang="en">
<head>
<meta charset="utf-8">
<title>Rules Poster</title>
<link rel="stylesheet" href="https://fonts.googleapis.com/css2?family=Fira+Sans:wght@500;600;700&display=swap">
<style>
  :root {
    --backdrop: #d9d9d9;
    --sheet: #f2f2f2;
    --teal: #6aa9a8;
    --orange: #d2662f;
    --ink: #2e2a31;
    --slate: #5f5b67;
    --tan: #caa693;
    --rust: #9b5531;
    --olive: #9aa038;
    --red: #c84337;
    --mustard: #efb75c;
    --taupe: #7a6354;
    --white: #f7f5f2;
    --gold: #f7cf76;
    --peach: #f1c48c;
    --dark-text: #35302e;
  }
  * { box-sizing: border-box; margin: 0; padding: 0; }
  html, body { width: 1200px; height: 886px; overflow: hidden; }
  body {
    background: var(--backdrop);
    font-family: "Fira Sans", sans-serif;
    display: flex;
    align-items: center;
    justify-content: center;
  }
  .poster {
    width: 610px;
    height: 856px;
    background: linear-gradient(180deg, #f6f6f6, var(--sheet));
    box-shadow: 0 6px 20px rgba(0,0,0,0.18);
    padding: 34px 0 30px;
    display: flex;
    flex-direction: column;
    justify-content: space-between;
  }
  .rule {
    filter: drop-shadow(0 4px 3px rgba(0,0,0,0.28));
    margin-right: 8px;
  }
  .rule__band {
    height: 68px;
    display: flex;
    align-items: center;
    justify-content: center;
    padding: 0 14px;
    clip-path: polygon(0 12%, 100% 0, 100% 100%, 0 88%);
  }
  .rule:nth-child(even) .rule__band { clip-path: polygon(0 0, 100% 12%, 100% 88%, 0 100%); }
  .rule__text {
    width: 100%;
    text-align: center;
    font-weight: 600;
    line-height: 1.25;
    white-space: nowrap;
  }
  .rule__text--lg { font-size: 27px; }
  .rule__text--md { font-size: 22px; }
  .rule__text--sm { font-size: 19.5px; }
  .rule__text--xs { font-size: 15.5px; font-weight: 500; text-align: left; }
  .rule__text--xs .line { display: block; }
  .rule__text--xs .line--tail { text-align: right; }

  .rule--writing .rule__band { background: var(--teal); color: var(--white); }
  .rule--record .rule__band { background: var(--orange); color: var(--gold); }
  .rule--record .accent { color: var(--white); }
  .rule--private .rule__band { background: var(--ink); color: var(--gold); }
  .rule--numbers .rule__band { background: var(--slate); color: var(--peach); }
  .rule--breaks .rule__band { background: var(--tan); color: var(--dark-text); }
  .rule--money .rule__band { background: var(--rust); color: var(--white); }
  .rule--depends .rule__band { background: var(--olive); color: var(--dark-text); }
  .rule--depends .accent { color: var(--white); }
  .rule--campaign .rule__band { background: var(--red); color: var(--gold); }
  .rule--assume .rule__band { background: var(--mustard); color: var(--dark-text); }
  .rule--assume .rule__text { font-size: 26px; font-weight: 700; }
  .rule--mistake .rule__band { background: var(--taupe); color: var(--white); }
  .rule--mistake .rule__text { font-size: 16.5px; }
</style>
</head>
<body>
  <main class="poster">
    <div class="rule rule--writing"><div class="rule__band"><p class="rule__text rule__text--lg">If it’s not in writing it doesn’t exist</p></div></div>
    <div class="rule rule--record"><div class="rule__band"><p class="rule__text rule__text--lg">No such thing as <span class="accent">“off the record”</span></p></div></div>
    <div class="rule rule--private"><div class="rule__band"><p class="rule__text rule__text--sm">Do not hold a private conversation in a public place</p></div></div>
    <div class="rule rule--numbers"><div class="rule__band"><p class="rule__text rule__text--md">Don’t believe any number that ends in zero</p></div></div>
    <div class="rule rule--breaks"><div class="rule__band"><p class="rule__text rule__text--sm">Never turn down an opportunity to eat or go to the bathroom</p></div></div>
    <div class="rule rule--money"><div class="rule__band"><p class="rule__text rule__text--xs"><span class="line">Don’t spend any of your own money. Don’t even admit you own a credit card.</span><span class="line line--tail">Don’t spend money that is not yours.</span></p></div></div>
    <div class="rule rule--depends"><div class="rule__band"><p class="rule__text rule__text--sm">Not always a <span class="accent">“right”</span> or <span class="accent">“wrong”</span> answer - <span class="accent">“It depends”</span></p></div></div>
    <div class="rule rule--campaign"><div class="rule__band"><p class="rule__text rule__text--xs"><span class="line">In a campaign, someone has to be in charge – campaigns are a place to foster</span><span class="line line--tail">democracy, not practice it.</span></p></div></div>
    <div class="rule rule--assume"><div class="rule__band"><p class="rule__text">Assume nothing</p></div></div>
    <div class="rule rule--mistake"><div class="rule__band"><p class="rule__text">If you make a mistake, fix it before analyzing. Bad news doesn’t age well</p></div></div>
  </main>
</body>
</html>
```